Flyer Design Project

I need a flyer design to pass out to promote my business and to bring in more business. My business is a auto body shop and we do auto body repair on all makes and models. We take all types of insurance work and cash deals are welcome. We type of paint we use is KTV so i would like the KTV logo somewhere on the flyer.I would also like to include that we offer free estimates.
Updates

I forgot to include the following information to my shop

Address : 3847 N. Willowmere St
                 San Mateo, Ca 94402

Tel : 650-318-4962

Website : www.TrueLineCollision.example

please include that cash deals are welcome, we offer 24 hours drop off service, and we offer mobile estimate service

Industry/Entity Type

Insurance

Requirements
Must have
• Must have my company logo in it. Must be eye catching.

```html
<!DOCTYPE html>
<html lang="en">
<head>
<meta charset="utf-8">
<title>TrueLine Auto Body Shop – Flyer</title>
<link href="https://fonts.googleapis.com/css2?family=Roboto+Condensed:ital,wght@0,700;1,400;1,700;1,800&display=swap" rel="stylesheet">
<style>
  :root {
    --ink: #1d1b1c;
    --night: #141213;
    --red: #c8202f;
    --paper: #d3d3d5;
    --white: #ffffff;
    --chrome-light: #c9cbcd;
    --chrome-dark: #3a3c3f;
  }
  html, body { margin: 0; padding: 0; overflow: hidden; background: var(--paper); }
  .flyer {
    position: relative;
    width: 857px;
    height: 1200px;
    overflow: hidden;
    background: var(--paper);
    font-family: "Roboto Condensed", "Arial Narrow", sans-serif;
    font-style: italic;
  }
  .backdrop { position: absolute; inset: 0; }
  .contact {
    position: absolute;
    right: 40px;
    top: 48px;
    text-align: right;
    color: var(--white);
    font-weight: 800;
    line-height: 1;
  }
  .contact__phone { font-size: 46px; letter-spacing: 0.5px; }
  .contact__web { font-size: 27px; margin-top: 4px; }
  .address {
    position: absolute;
    left: 78px;
    top: 676px;
    color: var(--white);
    font-weight: 700;
    font-size: 31px;
    line-height: 44px;
  }
  .brand {
    position: absolute;
    left: 405px;
    top: 790px;
    width: 240px;
    display: flex;
    align-items: center;
    gap: 10px;
    color: var(--red);
    font-weight: 800;
    font-size: 36px;
    line-height: 1;
  }
  .brand__dot {
    width: 30px; height: 30px; border-radius: 50%;
    background: var(--red); flex: none;
  }
  .perks {
    position: absolute;
    left: 40px;
    width: 305px;
    top: 868px;
    text-align: right;
    font-weight: 700;
    line-height: 1;
  }
  .perks__lead { color: var(--red); font-size: 45px; font-weight: 800; display: block; }
  .perks__tail { color: var(--ink); font-size: 41px; display: block; margin-bottom: 12px; }
  .about {
    position: absolute;
    left: 370px;
    top: 920px;
    width: 452px;
    margin: 0;
    color: var(--ink);
    font-weight: 700;
    font-size: 13.6px;
    line-height: 23.2px;
    text-align: justify;
  }
</style>
</head>
<body>
<main class="flyer">
  <svg class="backdrop" width="857" height="1200" viewBox="0 0 857 1200" aria-hidden="true">
    <defs>
      <linearGradient id="showroom" x1="0" y1="0" x2="0" y2="1">
        <stop offset="0" stop-color="#1a1a1c"/>
        <stop offset="0.45" stop-color="#b9bcbf"/>
        <stop offset="0.7" stop-color="#5d6064"/>
        <stop offset="1" stop-color="#141415"/>
      </linearGradient>
    </defs>
    <!-- dark upper field -->
    <rect class="field-dark" x="0" y="0" width="857" height="900" fill="var(--night)"/>
    <!-- top red band -->
    <polygon class="band-top" points="30,0 120,0 857,232 857,262" fill="var(--red)"/>
    <!-- lower red band behind address -->
    <polygon class="band-address" points="0,540 0,556 857,822 857,806" fill="var(--red)"/>
    <!-- light lower panel -->
    <polygon class="field-light" points="0,893 560,722 857,814 857,1200 0,1200" fill="var(--paper)"/>
    <!-- red edge of light panel -->
    <polygon class="band-panel" points="0,872 590,692 640,706 0,893" fill="var(--red)"/>
  </svg>

  <svg class="photo" style="position:absolute;left:0;top:140px" width="857" height="520" viewBox="0 0 857 520" role="img" aria-label="Photo of a silver sports car on a glossy dark showroom floor">
    <path d="M0 20 Q420 -20 820 230 L830 420 L0 470 Z" fill="url(#showroom)" opacity="0.9"/>
  </svg>

  <div class="contact">
    <div class="contact__phone">650-318-4962</div>
    <div class="contact__web">www.TrueLineCollision.example</div>
  </div>

  <div class="address">
    3847 N. Willowmere St<br>
    San Mateo, Ca 94402
  </div>

  <div class="brand">
    <span class="brand__dot"></span>
    <span class="brand__name">TrueLine</span>
  </div>

  <div class="perks">
    <span class="perks__lead">CASH DEALS</span>
    <span class="perks__tail">are welcome</span>
    <span class="perks__lead">24 HOUR</span>
    <span class="perks__tail">drop off service</span>
    <span class="perks__lead">MOBILE</span>
    <span class="perks__tail">estimate service</span>
  </div>

  <p class="about">At TrueLine auto body shop your entire repair is done to your outmost satisfaction. We know how important your vehicle is to you. Therefore we will ensure all vehicles are expertly restored to the highest possible standards. Due to our wealth of experience, we are equipped to handle variety of vehicles, imports and domestic. All of our staff is fully trained and competent with all the modern techniques associated with the vehicle repair industry. Our certified technicians specialize in full repairs of metal, plastic, fiberglass and more. We pride in our courteous, efficient and quality service combined with competitive pricing. At TrueLine Auto Body Shop all of our equipment follows innovative standards and is continuously upgraded to meet the demands of the automobile industry.</p>
</main>
</body>
</html>
```